Velbrook App Homepage Design making customers feel in control of their spend

Hi,
We need a App Homepage design with a UI similar to the attached mock up on an Quillo 4. The app is intended to put customers in control of their usage and spend on their fixed phone, broadband, mobile, gas and electricity.

Please fee free to propose improvements to the background images, icons, colours, etc.

Any questions please let me know.

Thanks
Tomasz

Target Market(s)

Consumer customers

Industry/Entity Type

Internet

Font styles to use
Sans Serif

Colors
3276b5
0255a3
85acd3
cfdeed
ffffff

Requirements
Must have
• Content in line with the guidelines in the attached mock up

```html
<!DOCTYPE html>
<html lang="en">
<head>
<meta charset="utf-8">
<title>Velbrook – Home</title>
<link rel="stylesheet" href="https://fonts.googleapis.com/css2?family=Lato:wght@400;700;900&display=swap">
<style>
  :root{
    --stage:#eef1f5;
    --white:#ffffff;
    --mist:#f7f7f7;
    --navy:#0a2d6e;
    --navy-deep:#01214f;
    --ink-grey:#8a8a8a;
    --lime:#c6d33a;
    --gold:#f5c518;
    --orange:#f5a623;
    --muted-blue:#6b86b8;
    --text:#111111;
  }
  *{box-sizing:border-box;margin:0;padding:0}
  html,body{width:1200px;height:1200px;overflow:hidden}
  body{background:var(--stage);font-family:"Lato",sans-serif;position:relative}
  .screen{position:absolute;top:212px;width:436px;height:775px;overflow:hidden;background:var(--white)}
  .screen--light{left:114px}
  .screen--dark{left:650px}
  .status-bar{position:absolute;top:0;left:0;right:0;height:24px;font-size:13px;color:var(--text);display:flex;align-items:center;justify-content:space-between;padding:0 8px}
  .status-bar__time{position:absolute;left:0;right:0;text-align:center;pointer-events:none}
  .status-bar__battery{display:flex;align-items:center;gap:4px}
  .battery{width:26px;height:11px;border:1px solid var(--text);border-radius:2px;padding:1px}
  .battery span{display:block;height:100%;background:var(--text)}
  .brand-header{position:absolute;top:24px;left:0;right:0;height:99px;display:flex;align-items:center;justify-content:center;gap:10px}
  .brand-header__dot{width:30px;height:30px;border-radius:50%;background:var(--navy)}
  .brand-header__name{font-size:28px;font-weight:900;color:var(--navy)}
  .summary{position:absolute;top:123px;left:0;right:0;height:527px}
  .screen--light .summary{background:var(--mist)}
  .screen--dark .summary{background:var(--navy)}
  .summary__label{position:absolute;top:34px;left:0;right:0;text-align:center;font-size:15px}
  .screen--light .summary__label{color:var(--ink-grey)}
  .screen--dark .summary__label{color:var(--gold)}
  .summary__amount{position:absolute;left:0;right:0;text-align:center;font-size:72px;font-weight:900;letter-spacing:1px}
  .screen--light .summary__amount{top:92px;color:var(--navy)}
  .screen--dark .summary__amount{top:62px;color:var(--white)}
  .bar{position:absolute;width:72px;bottom:0}
  .bar--calls{left:26px;background:linear-gradient(#6a3a96,#d4218a)}
  .bar--broadband{left:104px;background:linear-gradient(#2a5db0,#0a9fe3)}
  .bar--mobile{left:181px;background:linear-gradient(#7aa52a,#c7d82c)}
  .bar--gas{left:259px;background:linear-gradient(#e3402f,#f7a10a)}
  .bar--power{left:337px;background:linear-gradient(#c8203e,#f7378f)}
  .chart{position:absolute;left:0;right:0}
  .screen--light .chart{top:0;height:504px}
  .screen--dark .chart{top:0;height:441px}
  .bar .icon{position:absolute;left:18px;bottom:12px;width:36px;height:36px}
  .bar__value{position:absolute;left:0;right:0;bottom:10px;text-align:center;color:var(--white);font-size:14px}
  .icon-row{position:absolute;top:462px;left:0;right:0;height:40px}
  .icon-row .icon{position:absolute;top:0;width:40px;height:40px}
  .icon{fill:none;stroke:var(--white);stroke-width:1.6;stroke-linecap:round;stroke-linejoin:round}
  .bill{position:absolute;top:650px;left:0;right:0;height:125px;padding:0 25px}
  .screen--light .bill{background:var(--navy)}
  .screen--dark .bill{background:var(--navy-deep)}
  .bill__date{position:absolute;top:13px;left:25px;font-size:13px;color:var(--lime)}
  .bill__amount{position:absolute;top:36px;left:25px;font-size:27px;font-weight:700;color:var(--white)}
  .bill__renew{position:absolute;top:93px;left:25px;font-size:13px;color:var(--muted-blue)}
  .bill__support{position:absolute;top:93px;right:24px;font-size:13px;color:var(--orange)}
</style>
</head>
<body>
<svg width="0" height="0" style="position:absolute" aria-hidden="true">
  <defs>
    <symbol id="i-phone" viewBox="0 0 36 36"><path d="M9 6l5 0 2 7-3 2c1 4 4 7 8 8l2-3 7 2v5c0 1-1 2-2 2C17 29 7 19 7 8c0-1 1-2 2-2z"/><path d="M21 8a7 7 0 0 1 7 7M21 4a11 11 0 0 1 11 11"/></symbol>
    <symbol id="i-wifi" viewBox="0 0 36 36"><path d="M3 14a21 21 0 0 1 30 0M8 19a14 14 0 0 1 20 0M13 24a7 7 0 0 1 10 0"/><circle cx="18" cy="29" r="1.6"/></symbol>
    <symbol id="i-mobile" viewBox="0 0 36 36"><rect x="11" y="4" width="14" height="28" rx="2"/><path d="M11 8h14M11 27h14M16 6h4"/><circle cx="18" cy="29.5" r="1"/><path d="M7 13a6 6 0 0 0 0 6M4 11a10 10 0 0 0 0 10M29 13a6 6 0 0 1 0 6M32 11a10 10 0 0 1 0 10"/></symbol>
    <symbol id="i-flame" viewBox="0 0 36 36"><path d="M18 4c1 6 9 9 9 18a9 9 0 0 1-18 0c0-5 3-8 4-11 1 3 2 4 3 5 1-4 1-8 2-12z"/><path d="M15 27a3 3 0 0 0 6 0"/></symbol>
    <symbol id="i-plug" viewBox="0 0 36 36"><path d="M13 4v8M23 4v8M9 12h18v10a6 6 0 0 1-6 6h-6a6 6 0 0 1-6-6z"/><path d="M15 32h6M18 28v4"/><path d="M19 15l-3 5h4l-3 5"/></symbol>
  </defs>
</svg>

<section class="screen screen--light">
  <div class="status-bar"><span>●●●●● Nimbus</span><span class="status-bar__time">9:41 AM</span><span class="status-bar__battery">100% <span class="battery"><span></span></span></span></div>
  <header class="brand-header"><span class="brand-header__dot"></span><span class="brand-header__name">Velbrook</span></header>
  <div class="summary">
    <p class="summary__label">Your current total charges</p>
    <p class="summary__amount">$68.39</p>
    <div class="chart">
      <div class="bar bar--calls" style="height:139px"><svg class="icon"><use href="#i-phone"/></svg></div>
      <div class="bar bar--broadband" style="height:186px"><svg class="icon"><use href="#i-wifi"/></svg></div>
      <div class="bar bar--mobile" style="height:89px"><svg class="icon"><use href="#i-mobile"/></svg></div>
      <div class="bar bar--gas" style="height:210px"><svg class="icon"><use href="#i-flame"/></svg></div>
      <div class="bar bar--power" style="height:165px"><svg class="icon"><use href="#i-plug"/></svg></div>
    </div>
  </div>
  <footer class="bill">
    <p class="bill__date">Last bill on Dec 09, 2016</p>
    <p class="bill__amount">$75.76</p>
    <p class="bill__renew">Allowances renew in 18 days</p>
    <p class="bill__support">Call support</p>
  </footer>
</section>

<section class="screen screen--dark">
  <div class="status-bar"><span>●●●●● Nimbus</span><span class="status-bar__time">9:41 AM</span><span class="status-bar__battery">100% <span class="battery"><span></span></span></span></div>
  <header class="brand-header"><span class="brand-header__dot"></span><span class="brand-header__name">Velbrook</span></header>
  <div class="summary">
    <p class="summary__label">Your current total charges</p>
    <p class="summary__amount">$68.39</p>
    <div class="chart">
      <div class="bar bar--calls" style="height:139px"><span class="bar__value">$10.50</span></div>
      <div class="bar bar--broadband" style="height:186px"><span class="bar__value">$15.00</span></div>
      <div class="bar bar--mobile" style="height:89px"><span class="bar__value">$8.00</span></div>
      <div class="bar bar--gas" style="height:210px"><span class="bar__value">$20.50</span></div>
      <div class="bar bar--power" style="height:165px"><span class="bar__value">$14.39</span></div>
    </div>
    <div class="icon-row">
      <svg class="icon" style="left:42px"><use href="#i-phone"/></svg>
      <svg class="icon" style="left:120px"><use href="#i-wifi"/></svg>
      <svg class="icon" style="left:197px"><use href="#i-mobile"/></svg>
      <svg class="icon" style="left:275px"><use href="#i-flame"/></svg>
      <svg class="icon" style="left:353px"><use href="#i-plug"/></svg>
    </div>
  </div>
  <footer class="bill">
    <p class="bill__date">Last bill on Dec 09, 2016</p>
    <p class="bill__amount">$75.76</p>
    <p class="bill__renew">Allowances renew in 18 days</p>
    <p class="bill__support">Call support</p>
  </footer>
</section>
</body>
</html>
```